CODED website - Breakfree418

I am a successful entrepreneur - have recently sold my business and am semi-retired. I want to give something back, as well as provide a blog for articles and my journeys.

I will also be using this to provide free business and entrepreneurial advice.

I am creating a NOT FOR PROFIT business called Breakfree418.com.au which will provide the following;

1. Blog and articles; my travels, Small to Medium business advice and articles

2. My Bucket List - the 100 things I aim to achieve

3. Free business / start up advice - a section on the website which provides case studies on people / businesses which ask me for advice. We will then chronicle their story and what advice we have given for them to succeed.

My inspiration is the Martin Okonkwo idea and website;

http://martinokonkwo.example/about-martin/

Obviously I do NOT want a copy of this site, but use this for inspiration.

Furthermore, I would be interested in ongoing collaboration with the successful designer - I will be providing advice and consultancy to start ups, all of which will need web design etc, so there is ongoing referral streams for the successful designer.

I need this to be CODED and then uplifted to the website, so please DO NOT bid on this unless you can provide a coded site and facilitate the upload to WildHostings.

The NECESSARY tabs / pages

Main landing page - a short introduction into the ethos of Breakfree418

Writing - this will be the blog articles

About

Our Bucket List - a section where we can add our 100 buket list items. Hyperlinked to open a new page which has details on each bucket list item (ie #1 Make Breakfree418 - hyperlink to a new page which then has info on the bucklist item and what we have done)

Breakfree418 - this will be the section where we discuss people / businesses that we are helping. We will have an opening intro section + a link to the contact us page so they can ask us for the free advice. This will be the section where we have case studies into businesses / people that we have helped.
Updates

Hey everyone!

I'm really keen to get this website launched and looking amazing - if you have any questions, or would like to discuss anything at all, please email me at

dave@pinnaclepost.example.au

As I mentioned in the brief, I am doing this site to give back; I will not be earning a cent, and I will not be trying to earn any funds. I'm doing it simply to help other start ups or entrepreneurs, so I really want this site to look amazing.

I hope someone reads this and is inspired, and wants to be involved in this social enterprise with me.

Really excited to hear from you all and see your designs!

Industry/Entity Type

Business

Requirements
Must have
• MUST BE CODED and uplifted to the WildHosting registered domain - www.breakfree418.com.au - happy to discuss additional costings for this with successful designer.

Separate pages for each section (as outlined in the brief above)

Blog section to look similar to http://martinokonkwo.example/3x5/

Comprehensive website - not a simple wordpress template theme with some minor modifications. I will immediately reject any simple template design. I am looking for a slick, fully functioning website design.

PLEASE BE AWARE that I am looking for ongoing collaboration with the www.breakfree418.com.au.

I am trying this website as I want to find a young, energetic, vibrant, dynamic designer - this is your opportunity to be a part of something big, as this website will be huge!

Please do not submit a design if you are not motivated and ready for something big.

```html
<!DOCTYPE html>
<html lang="en">
<head>
<meta charset="utf-8">
<title>Breakfree418</title>
<link href="https://fonts.googleapis.com/css2?family=Source+Sans+3:wght@400;600&display=swap" rel="stylesheet">
<style>
:root{
  --sky:#d6ecf8;
  --brand:#1f78b8;
  --nav-top:#62c4f2;
  --nav-bottom:#2a9ee0;
  --ink:#2b2b2b;
  --body:#7a7a7a;
  --muted:#9a9a9a;
  --gold-top:#ffd21e;
  --gold-bottom:#f2b705;
  --panel:#f7f7f7;
  --line:#e3e3e3;
  --orange-top:#f6ac4d;
  --orange-bottom:#f08a1c;
  --foot-text:#fff6e8;
  --foot-dim:#ffe3bd;
}
*{margin:0;padding:0;box-sizing:border-box}
html,body{width:726px;height:1200px;overflow:hidden;background:#fff}
body{position:relative;font-family:"Source Sans 3",sans-serif;color:var(--ink)}
.abs{position:absolute}
.hero{left:0;top:0;width:726px;height:340px;background:linear-gradient(180deg,#8fcdf0 0%,var(--sky) 35%,#f4fafd 80%,#fff 100%)}
.hero-art{left:40px;top:118px;width:640px;height:200px;border-radius:40px 40px 80px 80px;background:radial-gradient(ellipse at 50% 60%,#c9b48a 0%,#9fbf7a 35%,#7cc0e6 70%,rgba(200,230,248,0) 100%)}
.logo{left:0;width:726px;top:22px;text-align:center;color:var(--brand);font-size:28px;font-weight:400;letter-spacing:.3px}
.slogan{left:0;width:726px;top:54px;text-align:center;color:var(--brand);font-size:11px}
.nav{left:16px;top:84px;width:676px;height:38px;border:2px solid #fff;border-radius:4px;background:linear-gradient(180deg,var(--nav-top),var(--nav-bottom));box-shadow:0 1px 4px rgba(0,60,120,.25)}
.nav a{position:absolute;top:11px;color:#fff;font-size:11.5px;text-decoration:none;letter-spacing:.2px}
.nav i{position:absolute;top:11px;width:1px;height:14px;background:rgba(255,255,255,.6)}
.dots{left:343px;top:313px}
.dots span{display:inline-block;width:5px;height:5px;border-radius:50%;background:#fff;margin-right:2px}
h2.section{left:27px;top:347px;font-size:16px;font-weight:400}
.photo{border-radius:0}
p.copy{font-size:8.5px;line-height:13px;color:var(--body)}
.title{font-size:11px;color:#333}
.card-head{font-size:11px;color:#333}
.more{font-size:8px;color:#222}
.side{left:486px;top:350px;width:202px;height:640px;background:var(--panel);border:1px solid var(--line);border-radius:4px}
.side-head{left:486px;width:202px;height:32px;background:linear-gradient(180deg,var(--gold-top),var(--gold-bottom));border-radius:3px 3px 0 0;color:#333;font-size:12.5px;padding:8px 0 0 18px}
.bucket{left:509px;font-size:8.5px;color:#555}
.bucket b{display:inline-block;width:9px;height:9px;border-radius:50%;background:#e6e6e6;margin-right:7px;vertical-align:-1px;position:relative}
.bucket b::after{content:"";position:absolute;left:3.5px;top:2.5px;border-left:3px solid #666;border-top:2px solid transparent;border-bottom:2px solid transparent}
.post-t{left:503px;font-size:10px;color:#777}
.post-s{left:503px;font-size:7.5px;line-height:13px;color:#999}
.footer{left:19px;top:1009px;width:673px;height:191px;background:linear-gradient(180deg,var(--orange-top),var(--orange-bottom));border-radius:4px 4px 0 0}
.foot-bar{left:19px;top:1170px;width:673px;height:30px;background:#f7b25c}
.foot-h{font-size:12px;color:#fff}
.foot-l{font-size:8px;color:var(--foot-text)}
.foot-div{width:1px;height:125px;background:rgba(255,255,255,.45);top:1030px}
.year{font-size:10.5px;color:#fff;line-height:10px}
.year small{display:block;font-size:6.5px;color:var(--foot-dim);line-height:9px}
.arrow{display:inline-block;border-left:3px solid var(--foot-dim);border-top:3px solid transparent;border-bottom:3px solid transparent;margin-right:6px}
.social{top:1175px;width:18px;height:18px;border-radius:50%;background:#f08a1c}
</style>
</head>
<body>

<div class="abs hero"></div>
<div class="abs hero-art" role="img" aria-label="Illustration of world landmarks on an island surrounded by waves and sky"></div>
<div class="abs logo">Breakfree418</div>
<div class="abs slogan">your slogan goes here</div>

<nav class="abs nav">
  <a style="left:34px">HOME</a><i style="left:86px"></i>
  <a style="left:99px">ABOUT US</a><i style="left:168px"></i>
  <a style="left:187px">TRAVEL PLACES</a><i style="left:282px"></i>
  <a style="left:302px">LATEST ARTICLES</a><i style="left:410px"></i>
  <a style="left:424px">ADVICES</a><i style="left:485px"></i>
  <a style="left:504px">SOLUTIONS</a><i style="left:580px"></i>
  <a style="left:598px">CONTACT</a>
</nav>
<div class="abs dots"><span></span><span></span><span></span></div>

<h2 class="abs section">Latest Articles</h2>

<div class="abs photo" style="left:26px;top:379px;width:124px;height:102px;background:linear-gradient(135deg,#c9b8a0,#8a98a8 60%,#d8d2c8)" role="img" aria-label="Photo of a couple taking a travel picture"></div>
<div class="abs title" style="left:161px;top:377px">Pellentesque habitant morbi tristique senectus</div>
<p class="abs copy" style="left:161px;top:396px;width:300px">Mauris vel lacus vitae felis vestibulum volutpat. Etiam est nunc, venenatis in, tristique eu, imperdiet ac, nisl. Cum sociis natoque penatibus et magnis dis parturient montes, nascetur ridiculus mus. In iaculis facilisis massa. Etiam eu urna.</p>
<p class="abs copy" style="left:161px;top:454px;width:300px">Sed porta. Suspendisse quam leo, molestie sed, luctus quis, feugiat in, pede. Fusce tellus. Sed metus augue, convallis et, vehicula ut, pulvinar eu, ante.</p>
<p class="abs copy" style="left:27px;top:491px;width:436px">Nunc tempus felis vitae urna. Vivamus porttitor, neque at volutpat rutrum, purus nisi eleifend libero, a tempus libero lectus feugiat felis. Morbi diam mauris, viverra in, gravida eu, mattis in, ante. Morbi eget arcu.</p>
<p class="abs copy" style="left:27px;top:521px;width:436px">Morbi porta, libero id ullamcorper nonummy, nibh ligula pulvinar metus, eget consectetuer augue nisi quis lacus. Ut ac mi quis lacus mollis aliquam. Curabitur iaculis tempus eros. Curabitur vel mi sit amet magna malesuada ultrices. Ut nisi erat, fermentum vel, congue id, euismod in, elit. Fusce ultricies, orci ac feugiat suscipit</p>

<!-- row 1 -->
<div class="abs card-head" style="left:26px;top:585px">Donec convallis pede venenatis</div>
<div class="abs photo" style="left:26px;top:607px;width:205px;height:87px;background:linear-gradient(90deg,#5a6470,#9aa6b2 55%,#c8d2da)" role="img" aria-label="Photo of a businessman beside a private jet"></div>
<div class="abs title" style="left:27px;top:699px">Pellentesque habitant morbi tristique senectus</div>
<p class="abs copy" style="left:27px;top:717px;width:205px">Mauris vel lacus vitae felis vestibulum volutpat. Etiam est nunc, venenatis in, tristique eu, imperdiet ac, nisl. Cum sociis natoque penatibus et magnis</p>
<div class="abs more" style="left:27px;top:761px">Learn More</div>

<div class="abs card-head" style="left:253px;top:585px">Mauris nunc quam venenatis nec</div>
<div class="abs photo" style="left:254px;top:607px;width:206px;height:87px;background:linear-gradient(180deg,#7fb6e0,#cfe4f2 45%,#efe9dc 60%,#e8a070 100%)" role="img" aria-label="Photo of a beach bag on white sand"></div>
<div class="abs title" style="left:255px;top:700px">Pellentesque habitant morbi tristique senectus</div>
<p class="abs copy" style="left:255px;top:718px;width:205px">Mauris vel lacus vitae felis vestibulum volutpat. Etiam est nunc, venenatis in, tristique eu, imperdiet ac, nisl. Cum sociis natoque penatibus et magnis</p>
<div class="abs more" style="left:255px;top:762px">Learn More</div>

<!-- row 2 -->
<div class="abs card-head" style="left:26px;top:801px">Sociis natoque penatibus</div>
<div class="abs photo" style="left:26px;top:822px;width:205px;height:80px;background:linear-gradient(90deg,#c9b49a,#e6e8ec 50%,#b8a48a)" role="img" aria-label="Photo of a couple in a historic square"></div>
<div class="abs title" style="left:27px;top:907px">Pellentesque habitant morbi tristique senectus</div>
<p class="abs copy" style="left:27px;top:925px;width:205px">Mauris vel lacus vitae felis vestibulum volutpat. Etiam est nunc, venenatis in, tristique eu, imperdiet ac, nisl. Cum sociis natoque penatibus et magnis</p>
<div class="abs more" style="left:27px;top:969px">Learn More</div>

<div class="abs card-head" style="left:254px;top:801px">Etiam est nunc venenatis</div>
<div class="abs photo" style="left:254px;top:822px;width:206px;height:80px;background:linear-gradient(180deg,#1e7fc8,#4aa6dc 60%,#d8e6e0 85%,#2b9ad0)" role="img" aria-label="Photo of an airliner flying over a coastline"></div>
<div class="abs title" style="left:255px;top:908px">Pellentesque habitant morbi tristique senectus</div>
<p class="abs copy" style="left:255px;top:926px;width:205px">Mauris vel lacus vitae felis vestibulum volutpat. Etiam est nunc, venenatis in, tristique eu, imperdiet ac, nisl. Cum sociis natoque penatibus et magnis</p>
<div class="abs more" style="left:255px;top:970px">Learn More</div>

<!-- sidebar -->
<div class="abs side"></div>
<div class="abs side-head" style="top:350px">Ethos of Breakfree418</div>
<div class="abs photo" style="left:493px;top:390px;width:190px;height:136px;background:linear-gradient(135deg,#c8d6e2,#6a7e9a 45%,#e0c8c8 75%,#b8c8d6)" role="img" aria-label="Video still of a family travelling with luggage"></div>
<svg class="abs" style="left:574px;top:444px" width="28" height="28" viewBox="0 0 28 28"><circle cx="14" cy="14" r="12.5" fill="#111" stroke="#fff" stroke-width="2"/><path d="M11 8.5 L19.5 14 L11 19.5Z" fill="#fff"/></svg>

<div class="abs side-head" style="top:550px;border-radius:0">My Bucket List</div>
<div class="abs bucket" style="top:592px"><b></b>Pellentesque habitant morbi</div>
<div class="abs bucket" style="top:613px"><b></b>Tristique senectus et</div>
<div class="abs bucket" style="top:635px"><b></b>Netus et malesuada fames</div>
<div class="abs bucket" style="top:656px"><b></b>Ac turpis egestas.</div>
<div class="abs bucket" style="top:677px"><b></b>Integer quis urna.</div>
<div class="abs bucket" style="top:699px"><b></b>Ut ante enim dapibus malesuada</div>
<div class="abs bucket" style="top:720px"><b></b>Fringilla eu condimentum</div>
<div class="abs bucket" style="top:742px"><b></b>Aenean porttitor eros vel dolor.</div>

<div class="abs side-head" style="top:774px;border-radius:0">Recent Blog Post</div>
<div class="abs post-t" style="top:817px">Mauris vel lacus vitae felis</div>
<div class="abs post-s" style="top:833px;width:175px">Cum sociis natoque penatibus et magnis dis parturient montes, nascetur ridiculus</div>
<div class="abs post-t" style="top:875px">Pellentesque habitant morbi</div>
<div class="abs post-s" style="top:891px">Cum sociis natoque penatibus et magnis dis</div>
<div class="abs post-t" style="top:919px">Aliquam vehicula mi at mauris</div>
<div class="abs post-s" style="top:935px">Cum sociis natoque penatibus et magnis dis</div>

<!-- footer -->
<footer class="abs footer"></footer>
<div class="abs foot-h" style="left:46px;top:1025px">Quick Links</div>
<div class="abs foot-l" style="left:50px;top:1054px;line-height:18.6px">Home<br>About Us<br>Video<br>Services<br>Articles</div>
<div class="abs foot-l" style="left:110px;top:1054px;line-height:18.6px">Most Viewed<br>Recent Blog<br>Archives<br>Category</div>
<div class="abs foot-l" style="left:190px;top:1054px;line-height:18.6px">Support<br>FAQ<br>Tips<br>Contact Us</div>
<div class="abs foot-div" style="left:254px"></div>
<div class="abs foot-h" style="left:280px;top:1025px">Recent Articles</div>
<div class="abs foot-l" style="left:280px;top:1052px;line-height:18.6px">
<span class="arrow"></span>Duis sed tellus et tortor vestibulum<br>
<span class="arrow"></span>Praesent elementum elit at tellus.<br>
<span class="arrow"></span>Curabitur metus ipsum<br>
<span class="arrow"></span>Luctus eu malesuada ut<br>
<span class="arrow"></span>Tincidunt sed diam.</div>
<div class="abs foot-div" style="left:443px"></div>
<div class="abs foot-h" style="left:472px;top:1025px">Archives</div>
<div class="abs year" style="left:472px;top:1052px">2012<small>click here</small></div>
<div class="abs year" style="left:523px;top:1052px">2009<small>click here</small></div>
<div class="abs year" style="left:570px;top:1052px">2006<small>click here</small></div>
<div class="abs year" style="left:472px;top:1084px">2011<small>click here</small></div>
<div class="abs year" style="left:523px;top:1084px">2008<small>click here</small></div>
<div class="abs year" style="left:570px;top:1084px">2005<small>click here</small></div>
<div class="abs year" style="left:472px;top:1116px">2010<small>click here</small></div>
<div class="abs year" style="left:523px;top:1116px">2007<small>click here</small></div>
<div class="abs year" style="left:570px;top:1116px">2004<small>click here</small></div>

<div class="abs foot-bar"></div>
<div class="abs" style="left:42px;top:1180px;font-size:7px;color:#7a4a10">Copyright © 2012 Company Name. All right reserved</div>
<div class="abs social" style="left:615px"></div>
<div class="abs social" style="left:635px"></div>
<div class="abs social" style="left:655px"></div>

</body>
</html>
```